Namecard Designs+Logo for a High End Automobile Company

We need a new business card for our company called Velta Motorhof.

www.veltamotorhof.example.sg
Our new website will be up in 2.5 months time.

We sell used and brand new continental cars like Stavaro, KTJ, Lindqvar, Castrelli and etc. Currently we are operating from 2 offices in Singapore and United Kingdom.

We want a design which is serious. We are open to colours but try to keep it at a maximum of 3 colours.

We prefer something simple and minimal. We are open to 2 sides printing or even 2 sided namecards. Both UK and Singapore company offices address must be in; either side by side, front and back, or even 2 sided cards.

The logo can be a text logo, emblem, abstract, pictorial or combination.

We are printing with Prinvo.example so please kindly follow the printing guideline.

http://uk.prinvo.example/help/faq/templates-and-guidelines.html

Target Market(s)

Rich and Car Enthusiasts

Industry/Entity Type

Printing

Requirements
Must have
• Our 2 offices; UK and Singapore.

Our slogan which is " The Automobile Specialist"
Should not have
• Not more than 3 colours

```html
<!DOCTYPE html>
<html lang="en">
<head>
<meta charset="utf-8">
<title>Velta Motorhof — Business Card</title>
<link rel="stylesheet" href="https://fonts.googleapis.com/css2?family=Noto+Serif:wght@400;700&display=swap">
<style>
  :root {
    --page: #ffffff;
    --brand-red: #e31b1b;
    --deep-red: #5a0508;
    --mid-red: #b50d10;
    --ink: #111111;
    --trim-line: #9a9a9a;
    --type-light: #f4e6e6;
  }
  html, body {
    margin: 0;
    padding: 0;
    width: 823px;
    height: 1200px;
    overflow: hidden;
    background: var(--page);
    font-family: "Noto Serif", Georgia, serif;
  }
  .sheet {
    position: relative;
    width: 823px;
    height: 1200px;
  }
  .trim-guide {
    position: absolute;
    border: 1px dotted var(--trim-line);
    box-sizing: border-box;
  }
  .trim-guide--front { left: 8px; top: 0; width: 814px; height: 588px; border-top: none; }
  .trim-guide--back  { left: 8px; top: 617px; width: 814px; height: 583px; border-bottom: none; }

  .card {
    position: absolute;
    left: 43px;
    width: 746px;
    height: 488px;
    border: 2px solid var(--brand-red);
    border-radius: 0 28px 0 28px;
    overflow: hidden;
    background: var(--page);
    box-sizing: border-box;
  }
  .card--front { top: 34px; }
  .card--back  { top: 679px; left: 41px; height: 490px; }

  .hero-photo {
    position: absolute;
    left: 0;
    width: 100%;
    background:
      radial-gradient(ellipse at 28% 62%, #ff2a22 0%, rgba(255,40,30,0) 45%),
      radial-gradient(ellipse at 92% 8%, #ff2a20 0%, rgba(255,40,30,0) 30%),
      radial-gradient(ellipse at 62% 40%, #2a0204 0%, rgba(42,2,4,0) 45%),
      linear-gradient(135deg, var(--mid-red) 0%, var(--deep-red) 55%, var(--mid-red) 100%);
  }
  .card--front .hero-photo { top: 173px; height: 315px; }
  .card--back .hero-photo  { top: 0; height: 407px; }

  .wordmark {
    position: absolute;
    text-align: left;
    color: var(--ink);
  }
  .wordmark__name {
    display: block;
    font-weight: 700;
    white-space: nowrap;
    line-height: 1;
  }
  .wordmark__slogan {
    display: block;
    font-weight: 700;
    white-space: nowrap;
    letter-spacing: 0.04em;
    margin-top: 10px;
  }
  .card--front .wordmark { right: 56px; top: 58px; }
  .card--front .wordmark__name { font-size: 31px; }
  .card--front .wordmark__slogan { font-size: 12.5px; text-align: right; }
  .card--back .wordmark { right: 55px; top: 420px; }
  .card--back .wordmark__name { font-size: 16px; }
  .card--back .wordmark__slogan { font-size: 7px; margin-top: 5px; text-align: right; }

  .office {
    position: absolute;
    top: 233px;
    color: var(--type-light);
    font-size: 16px;
    line-height: 1.2;
  }
  .office__title {
    margin: 0 0 14px;
    font-weight: 400;
    font-size: 24px;
    line-height: 1;
  }
  .office__title small { font-size: 16px; display: inline; }
  .office__address { margin: 0; font-style: normal; }
  .office--uk { left: 20px; width: 155px; text-align: right; }
  .office--sg { left: 229px; text-align: left; }
  .office--sg .office__title small { display: block; margin-top: 4px; }
</style>
</head>
<body>
<main class="sheet">
  <div class="trim-guide trim-guide--front"></div>
  <div class="trim-guide trim-guide--back"></div>

  <section class="card card--front" aria-label="Card front">
    <div class="wordmark">
      <span class="wordmark__name">Velta Motorhof</span>
      <span class="wordmark__slogan">The Automobile Specialist</span>
    </div>
    <div class="hero-photo" role="img" aria-label="Red-toned photo of a convertible sports car's front half against a dark smoky red background"></div>
  </section>

  <section class="card card--back" aria-label="Card back">
    <div class="hero-photo" role="img" aria-label="Close-up red-toned photo of a convertible sports car side and front wheel over a dark red ink texture"></div>

    <div class="office office--uk">
      <h2 class="office__title">UK <small>OFFICE</small></h2>
      <address class="office__address">18 Harlow Street.<br>City, London.</address>
    </div>
    <div class="office office--sg">
      <h2 class="office__title">SINGAPORE <small>OFFICE</small></h2>
      <address class="office__address">7 Kenbury Road<br>Block 4C<br>Singapore 208417</address>
    </div>

    <div class="wordmark">
      <span class="wordmark__name">Velta Motorhof</span>
      <span class="wordmark__slogan">The Automobile Specialist</span>
    </div>
  </section>
</main>
</body>
</html>
```